4 Seitiger DIN A4 Flyer für Angebote (DIN A3 gefaltet)
Zielgruppe
Ich handel und montiere z.B. Hochwertige Fenster, Türen und Parkett.
Zielgruppen sind: Architekten, Baufirmen, Hausbauer sowie Hausbesitzer und Sanierer
Aufgabenstellung
Die Farben aus meinem Logo: Grün, Antrazith, Schwarz.
Der 4 Seitige Flyer soll als Aktionsflyer in der Tageszeitung verteilt werden.
Im Innenteil des Flyers sollten Die Parkettböden und 2 Zimmertüren angeboten werden.
Die Texte :
zu den jeweiligen Bildern gehört der qm Preis und der Satz: "zb. Landhausdiele Eiche, geölt Format 2200x180mm, Nutzschicht 2,5mm"
Ansonsten weis ich nicht was noch textlich verkaufsfördernd wäre
Die Rückseite mit Anschrift, Aktions-Treppen Sanierung oder Neubau( ab 1450.- ), Außenverschalung.

```html
<!DOCTYPE html>
<html lang="de">
<head>
<meta charset="utf-8">
<title>Parkett &amp; Laminatböden – Angebote</title>
<link rel="stylesheet" href="https://fonts.googleapis.com/css2?family=Jost:wght@500;600&family=Playfair+Display:ital@1&display=swap">
<style>
  :root {
    --green: #8ab626;
    --anthracite: #3a3a3a;
    --ink: #333333;
    --page-left: #ffffff;
    --page-right: #ededed;
    --white: #ffffff;
  }
  * { box-sizing: border-box; margin: 0; padding: 0; }
  html, body { width: 1200px; height: 849px; overflow: hidden; }
  body { position: relative; font-family: "Jost", Arial, sans-serif; color: var(--ink); }

  .page { position: absolute; top: 0; height: 849px; width: 600px; }
  .page--left { left: 0; background: var(--page-left); }
  .page--right { left: 600px; background: var(--page-right); }

  .page-title {
    position: absolute; left: 29px; top: 52px;
    font-weight: 500; font-size: 39px; letter-spacing: 1px; color: var(--ink);
  }

  .offer { position: absolute; width: 542px; height: 171px; display: flex; }
  .offer__photo { position: relative; width: 293px; height: 100%; }
  .offer__info { width: 249px; height: 100%; padding: 24px 0 0 15px; color: var(--white); }
  .offer__info--dark { background: var(--anthracite); }
  .offer__info--green { background: var(--green); }

  .offer__name { font-weight: 500; font-size: 28px; line-height: 31px; letter-spacing: .5px; text-transform: uppercase; }
  .offer__specs { list-style: none; margin-top: 12px; font-family: "Playfair Display", Georgia, serif; font-style: italic; font-size: 13px; line-height: 18.5px; letter-spacing: 2.2px; }
  .offer__specs li::before { content: "• "; font-style: normal; }

  .price {
    position: absolute; width: 90px; height: 90px; border-radius: 50%;
    display: flex; flex-direction: column; align-items: center; justify-content: center;
    color: var(--white); font-weight: 600;
  }
  .price--green { background: var(--green); }
  .price--dark { background: var(--anthracite); }
  .price__amount { font-size: 38px; line-height: 36px; }
  .price__unit { font-family: "Jost", Arial, sans-serif; font-weight: 500; font-size: 11px; letter-spacing: 1.5px; margin-top: 2px; }
  .price__amount--door { font-size: 27px; line-height: 1; }
  .offer__photo .price { left: 189px; top: 69px; }

  .door-card { position: absolute; top: 487px; width: 264px; height: 333px; background: var(--white); }
  .door-card__title {
    height: 60px; display: flex; align-items: center; justify-content: center;
    color: var(--white); font-weight: 500; font-size: 27px; letter-spacing: 1px; text-transform: uppercase;
  }
  .door-card__title--green { background: var(--green); }
  .door-card__title--dark { background: var(--anthracite); }
  .door-card__photo { position: absolute; left: 64px; top: 60px; width: 136px; height: 266px; }
  .door-card .price { left: 157px; top: 220px; }
</style>
</head>
<body>

<section class="page page--left">
  <h1 class="page-title">PARKET &amp; LAMINATBÖDEN</h1>

  <article class="offer" style="left:29px; top:111px;">
    <div class="offer__photo" role="img" aria-label="Holzboden Eiche hell, geölt" style="background:linear-gradient(90deg,#c29862,#b78a55 50%,#c9a06a);">
      <div class="price price--green"><span class="price__amount">8€</span><span class="price__unit">pro m²</span></div>
    </div>
    <div class="offer__info offer__info--dark">
      <h2 class="offer__name">Landhausdiele<br>„Eiche“</h2>
      <ul class="offer__specs"><li>Format 2200x180mm,</li><li>Nutzschicht 2,5mm</li><li>geölt</li></ul>
    </div>
  </article>

  <article class="offer" style="left:29px; top:290px;">
    <div class="offer__info offer__info--green">
      <h2 class="offer__name">Landhausdiele<br>„Eiche“</h2>
      <ul class="offer__specs"><li>Format 2200x180mm,</li><li>Nutzschicht 2,5mm</li><li>geölt</li></ul>
    </div>
    <div class="offer__photo" role="img" aria-label="Holzboden Eiche dunkel geräuchert" style="background:linear-gradient(90deg,#5e3a22,#7a4a2a 50%,#6a3f24);">
      <div class="price price--dark"><span class="price__amount">8€</span><span class="price__unit">pro m²</span></div>
    </div>
  </article>

  <article class="offer" style="left:29px; top:469px;">
    <div class="offer__photo" role="img" aria-label="Holzboden Eiche Stabparkett" style="background:linear-gradient(90deg,#c89a6a,#bb8b5c 50%,#c99d6d);">
      <div class="price price--green"><span class="price__amount">8€</span><span class="price__unit">pro m²</span></div>
    </div>
    <div class="offer__info offer__info--dark">
      <h2 class="offer__name">Landhausdiele<br>„Eiche“</h2>
      <ul class="offer__specs"><li>Format 2200x180mm,</li><li>Nutzschicht 2,5mm</li><li>geölt</li></ul>
    </div>
  </article>

  <article class="offer" style="left:29px; top:649px;">
    <div class="offer__info offer__info--green">
      <h2 class="offer__name">Landhausdiele<br>„Eiche“</h2>
      <ul class="offer__specs"><li>Format 2200x180mm,</li><li>Nutzschicht 2,5mm</li><li>geölt</li></ul>
    </div>
    <div class="offer__photo" role="img" aria-label="Holzboden Nussbaum" style="background:linear-gradient(180deg,#7a6048,#5a4432 45%,#7b5f45);">
      <div class="price price--dark"><span class="price__amount">8€</span><span class="price__unit">pro m²</span></div>
    </div>
  </article>
</section>

<section class="page page--right">
  <article class="offer" style="left:29px; top:111px;">
    <div class="offer__photo" role="img" aria-label="Holzboden Eiche gekalkt" style="background:linear-gradient(90deg,#c9a886,#bf9c79 50%,#cbab8a);">
      <div class="price price--green"><span class="price__amount">8€</span><span class="price__unit">pro m²</span></div>
    </div>
    <div class="offer__info offer__info--dark">
      <h2 class="offer__name">Landhausdiele<br>„Eiche“</h2>
      <ul class="offer__specs"><li>Format 2200x180mm,</li><li>Nutzschicht 2,5mm</li><li>geölt</li></ul>
    </div>
  </article>

  <article class="offer" style="left:29px; top:290px;">
    <div class="offer__info offer__info--green">
      <h2 class="offer__name">Landhausdiele<br>„Eiche“</h2>
      <ul class="offer__specs"><li>Format 2200x180mm,</li><li>Nutzschicht 2,5mm</li><li>geölt</li></ul>
    </div>
    <div class="offer__photo" role="img" aria-label="Holzboden Eiche natur astig" style="background:linear-gradient(90deg,#d8b586,#cfa979 50%,#d9b88a);">
      <div class="price price--dark"><span class="price__amount">8€</span><span class="price__unit">pro m²</span></div>
    </div>
  </article>

  <article class="door-card" style="left:29px;">
    <h2 class="door-card__title door-card__title--green">Weisse Holztür</h2>
    <div class="door-card__photo" role="img" aria-label="Weiße Zimmertür mit Kassetten" style="background:linear-gradient(90deg,#e6e6e6,#f7f7f7 50%,#ececec);"></div>
    <div class="price price--dark"><span class="price__amount price__amount--door">220€</span></div>
  </article>

  <article class="door-card" style="left:307px;">
    <h2 class="door-card__title door-card__title--dark">Ureiche Tür</h2>
    <div class="door-card__photo" role="img" aria-label="Zimmertür in Eiche rustikal" style="background:linear-gradient(90deg,#c29a62,#d1aa73 50%,#c49c64);"></div>
    <div class="price price--green"><span class="price__amount price__amount--door">220€</span></div>
  </article>
</section>

</body>
</html>
```